New career and executive coaching business needs a business card design including logo

Company name: 'Harborline Growth Partners.' The aim of my coaching engagements is to help people improve their communication in the workplace and achieve their career goals. The process involves working with individuals to help them uncover their strengths and talents, then leverage those to improve their working lives. The Tavelle Inventory is the starting point to the process. I am after an exciting and interesting business card design (including logo)which is professional yet will still get people's attention.

Industry/Entity Type

Business

Contact Information for Business Card

Name: Gordon Halvey
Position: Owner
Address: 58 Merrowind Cres, Larkvale Vic 3108
Phone: 0481936045
Website: harborlinegrowth.com.au
Email: gordon@hgp.com.au

Colors
33a6d7
00a990
0355a3
3176b5

Requirements
Must have
• logo

```html
<!DOCTYPE html>
<html lang="en">
<head>
<meta charset="utf-8">
<title>Harborline Growth Partners – Business Card</title>
<link href="https://fonts.googleapis.com/css2?family=Cinzel:wght@500;600&family=Montserrat:wght@400;500&display=swap" rel="stylesheet">
<style>
  :root{
    --navy:#0355a3;
    --mid-blue:#3176b5;
    --sky:#33a6d7;
    --teal:#00a990;
    --ink:#2d5f8f;
    --grey:#7d8690;
    --paper:#ffffff;
    --stage:#e6e9ed;
  }
  *{box-sizing:border-box;margin:0;padding:0}
  html,body{width:1200px;height:1023px;overflow:hidden;background:var(--stage)}
  .canvas{position:relative;width:1200px;height:1023px}

  .card{position:absolute;width:520px;height:300px;border-radius:4px;overflow:hidden;
        box-shadow:0 6px 18px rgba(0,0,0,.18)}
  .card--front{left:50px;top:150px;background:var(--paper)}
  .card--back{left:630px;top:150px;
        background:linear-gradient(135deg,var(--mid-blue) 0%,var(--navy) 70%,#02447f 100%)}

  .band{position:absolute;inset:0}

  .brand{position:absolute;display:flex;align-items:center;gap:12px;font-family:"Cinzel",serif;font-weight:600}
  .brand__dot{border-radius:50%;flex:none}
  .brand__text{line-height:1.05}
  .brand__name{display:block;letter-spacing:.04em}
  .brand__tag{display:block;letter-spacing:.12em}

  .card--front .brand{left:30px;top:38px;color:var(--navy)}
  .card--front .brand__dot{width:34px;height:34px;background:var(--navy)}
  .card--front .brand__name{font-size:28px}
  .card--front .brand__tag{font-size:11px;margin-top:3px}

  .person{position:absolute;left:30px;top:128px}
  .person__name{font-family:"Cinzel",serif;font-weight:500;font-size:21px;color:var(--ink);letter-spacing:.05em}
  .person__role{font-family:"Montserrat",sans-serif;font-size:10px;color:var(--grey);letter-spacing:.18em;margin-top:4px}

  .badges{position:absolute;right:28px;top:30px;display:flex;gap:18px;align-items:center}
  .badge--round{width:58px;height:58px;border-radius:50%;background:linear-gradient(135deg,var(--teal),var(--sky))}
  .badge--square{width:54px;height:54px;border-radius:8px;background:#d9dee3}

  .contacts{position:absolute;left:30px;top:204px;list-style:none;font-family:"Montserrat",sans-serif;font-size:11px;line-height:14px;color:#fff}
  .contacts li{display:flex;align-items:center;gap:8px;margin-bottom:5px;white-space:nowrap}
  .contacts svg{width:13px;height:13px;flex:none}
  .contacts .contacts__address{letter-spacing:.06em;margin-top:2px}

  .card--back .brand{left:50%;top:50%;transform:translate(-50%,-50%);flex-direction:column;text-align:center;color:#fff;gap:14px}
  .card--back .brand__dot{width:40px;height:40px;background:#fff}
  .card--back .brand__name{font-size:30px}
  .card--back .brand__tag{font-size:12px;margin-top:5px}

  .lockup{position:absolute;left:50%;top:640px;transform:translateX(-50%);flex-direction:column;text-align:center;color:var(--navy);gap:18px}
  .lockup .brand__dot{width:70px;height:70px;background:var(--navy)}
  .lockup .brand__name{font-size:52px}
  .lockup .brand__tag{font-size:20px;margin-top:8px}
</style>
</head>
<body>
<main class="canvas">

  <section class="card card--front" aria-label="Business card front">
    <svg class="band" viewBox="0 0 520 300" aria-hidden="true">
      <defs>
        <linearGradient id="bandFill" x1="0" y1="0" x2="1" y2="1">
          <stop offset="0" stop-color="#3f92cc"/>
          <stop offset="1" stop-color="#0355a3"/>
        </linearGradient>
      </defs>
      <polygon points="0,192 300,192 360,128 520,128 520,300 0,300" fill="url(#bandFill)"/>
    </svg>

    <div class="brand">
      <span class="brand__dot"></span>
      <span class="brand__text">
        <span class="brand__name">HARBORLINE</span>
        <span class="brand__tag">GROWTH PARTNERS</span>
      </span>
    </div>

    <div class="badges">
      <span class="badge badge--square" role="img" aria-label="Coaching accreditation badge"></span>
      <span class="badge badge--round" role="img" aria-label="Tavelle Inventory badge"></span>
    </div>

    <div class="person">
      <p class="person__name">GORDON HALVEY</p>
      <p class="person__role">OWNER</p>
    </div>

    <ul class="contacts">
      <li>
        <svg viewBox="0 0 16 16" aria-hidden="true"><rect width="16" height="16" rx="2" fill="#fff"/><path d="M5 3.5l2 2-1 1.2a7 7 0 0 0 3.3 3.3l1.2-1 2 2-1 1.5C7.5 12 4 8.5 3.5 4.5z" fill="#0355a3"/></svg>
        0481936045
      </li>
      <li>
        <svg viewBox="0 0 16 16" aria-hidden="true"><rect width="16" height="16" rx="2" fill="#fff"/><rect x="3" y="4.5" width="10" height="7" fill="none" stroke="#0355a3" stroke-width="1.3"/><path d="M3 4.5l5 4 5-4" fill="none" stroke="#0355a3" stroke-width="1.3"/></svg>
        gordon@hgp.com.au
      </li>
      <li>
        <svg viewBox="0 0 16 16" aria-hidden="true"><rect width="16" height="16" rx="2" fill="#fff"/><circle cx="8" cy="8" r="4.5" fill="none" stroke="#0355a3" stroke-width="1.2"/><path d="M3.5 8h9M8 3.5c-2 2.5-2 6.5 0 9M8 3.5c2 2.5 2 6.5 0 9" fill="none" stroke="#0355a3" stroke-width="1"/></svg>
        harborlinegrowth.com.au
      </li>
      <li class="contacts__address">58 MERROWIND CRES, LARKVALE VIC 3108</li>
    </ul>
  </section>

  <section class="card card--back" aria-label="Business card back">
    <div class="brand">
      <span class="brand__dot"></span>
      <span class="brand__text">
        <span class="brand__name">HARBORLINE</span>
        <span class="brand__tag">GROWTH PARTNERS</span>
      </span>
    </div>
  </section>

  <div class="brand lockup" aria-label="Harborline Growth Partners logo">
    <span class="brand__dot"></span>
    <span class="brand__text">
      <span class="brand__name">HARBORLINE</span>
      <span class="brand__tag">GROWTH PARTNERS</span>
    </span>
  </div>

</main>
</body>
</html>
```